Wellness Flyer

I am seeking a flyer for my health and wellness company, Orchard Vita. The flyer is to be DL size and single-sided. I am looking for a flyer that is both professional and fun looking, something similar to the uploaded files. Wording to include: (Please not wording to not include company name or logo but is rather advertising nutritional cleansing products)

Be your healthiest self. Take charge of your life. Get your best body.
Lose weight / Build muscle / Gain energy / Increase clarity
Start your journey to health and wellness. Transform your life
www.orchardvita.com.au
Mirela@orchardvita.com.au.
Natural . Raw. Organic . Cleansing system
Updates

Flyer needs to be single sided, DL size. I haven't uploaded my logo because I wanted to steer clear of having it on the flyer as it limits colour choice. Thanks.

Target Market(s)

Primarily Women 18-50.

Industry/Entity Type

Advertising

Font styles to use
Serif

Colors
34b8a4
fbed24

Requirements
Must have
• The wording as above.
Should not have
• Company name or Company logo

```html
<!DOCTYPE html>
<html lang="en">
<head>
<meta charset="utf-8">
<title>Wellness Flyer</title>
<link href="https://fonts.googleapis.com/css2?family=Bebas+Neue&family=Quicksand:wght@500&family=Open+Sans:wght@700&display=swap" rel="stylesheet">
<style>
  :root {
    --backdrop: #232323;
    --paper: #ffffff;
    --teal: #4fc0c6;
    --teal-soft: #a7dbe0;
    --orange: #f0894a;
    --tag-blue: #19b5d3;
    --tag-green: #8dc63f;
    --tag-orange: #fbb040;
    --tag-mauve: #c6a8b5;
    --band-green: #8dc63f;
    --band-rose: #dc7d7c;
  }
  * { margin: 0; padding: 0; box-sizing: border-box; }
  html, body { width: 1200px; height: 1000px; overflow: hidden; background: var(--backdrop); }
  .flyer {
    position: absolute; left: 422px; top: 82px;
    width: 433px; height: 864px;
    background: var(--paper);
    overflow: hidden;
  }
  .display { font-family: "Bebas Neue", sans-serif; line-height: 1; position: absolute; white-space: nowrap; }
  .kicker { left: 25px; top: 28px; font-size: 25.3px; color: var(--teal); letter-spacing: 0; }
  .headline-top { left: 25px; top: 50px; font-size: 100px; color: var(--teal); letter-spacing: 1.4px; }
  .headline-bottom { left: 25px; top: 131px; font-size: 116px; color: var(--orange); letter-spacing: 3.8px; }
  .promises { position: absolute; left: 0; top: 258px; width: 100%; text-align: center; list-style: none; }
  .promises li { font-family: "Bebas Neue", sans-serif; font-size: 32.5px; line-height: 48px; color: var(--teal-soft); }
  .photo {
    position: absolute; left: 0; top: 418px; width: 433px; height: 364px;
    background: linear-gradient(180deg, #fbfbfd 0%, #eef2f6 45%, #d6e6ee 62%, #c9dcc0 82%, #8cb54a 92%, #6f9a2e 100%);
  }
  .benefit {
    position: absolute; font-family: "Quicksand", sans-serif; font-weight: 500;
    color: #fff; white-space: nowrap; display: flex; align-items: center; justify-content: center;
  }
  .benefit--weight { left: 178px; top: 490px; width: 135px; height: 27px; background: var(--tag-blue); font-size: 16px; }
  .benefit--muscle { left: 203px; top: 517px; width: 135px; height: 27px; background: var(--tag-green); font-size: 16px; }
  .benefit--energy { left: 230px; top: 545px; width: 136px; height: 27px; background: var(--tag-orange); font-size: 16px; }
  .benefit--clarity { left: 259px; top: 573px; width: 146px; height: 21px; background: var(--tag-mauve); font-size: 13px; }
  .values {
    position: absolute; left: 0; top: 782px; width: 100%; height: 25px;
    background: var(--band-green); color: #fff;
    font-family: "Open Sans", sans-serif; font-weight: 700; font-size: 15px;
    display: flex; align-items: center; justify-content: center; gap: 9px;
  }
  .contact {
    position: absolute; left: 0; top: 813px; width: 100%; height: 51px;
    background: var(--band-rose); color: #fff;
    font-family: "Open Sans", sans-serif; font-weight: 700; font-size: 15px;
    text-align: center; line-height: 20px; padding-top: 7px;
  }
</style>
</head>
<body>
  <main class="flyer">
    <p class="display kicker">Start your journey to health and wellness.</p>
    <h1 class="display headline-top">TRANSFORM</h1>
    <h2 class="display headline-bottom">YOUR LIFE</h2>
    <ul class="promises">
      <li>Be your healthiest self.</li>
      <li>Take charge of your life.</li>
      <li>Get your best body.</li>
    </ul>
    <div class="photo" role="img" aria-label="Photo of a smiling woman in a mint tank top stretching on the grass by a river, city skyline behind"></div>
    <span class="benefit benefit--weight">LOSE WEIGHT</span>
    <span class="benefit benefit--muscle">BUILD MUSCLE</span>
    <span class="benefit benefit--energy">GAIN ENERGY</span>
    <span class="benefit benefit--clarity">INCREASE CLARITY</span>
    <div class="values">
      <span>Natural</span><span>•</span><span>Raw</span><span>•</span><span>Organic</span><span>•</span><span>Cleansing system</span>
    </div>
    <div class="contact">
      <div>www.orchardvita.com.au</div>
      <div>Mirela@orchardvita.com.au</div>
    </div>
  </main>
</body>
</html>
```